Business Card Design

We need a business card for a new business based in Sydney, Australia. It is a home based baking business, the key products are cookies and muffins and slices including gluten free baked goods. With the emphasis on home made baking. The target market is cafes, coffee shops and vans, restaurants. Products may be provided in display jars or individually wrapped. The final design should be in the colours pink, purple.

Industry/Entity Type

Business

Contact Information for Business Card

Pindle's Bakery Pty Ltd, Maren Tulloch, maren@pindlesbakery.com.au
0412 506 218, www.pindlesbakery.com.au, ACN 581 246 037,

```html
<!DOCTYPE html>
<html lang="en">
<head>
<meta charset="utf-8">
<title>Pindle's Bakery – Business Card</title>
<link href="https://fonts.googleapis.com/css2?family=Chewy&family=Delius&display=swap" rel="stylesheet">
<style>
  :root {
    --page-bg: #efeae6;
    --sky: #bfe6f0;
    --sky-deep: #a9dbe8;
    --band: #f7b3cc;
    --band-light: #fbcfe0;
    --lace: #f3a3c0;
    --lace-white: #fff6fa;
    --ring: #ea8fb1;
    --cupcake-pink: #f27aa8;
    --cupcake-cream: #fde6ef;
    --ink-pink: #d9226c;
    --ink-dark: #2b2226;
  }
  * { margin: 0; padding: 0; box-sizing: border-box; }
  html, body {
    width: 1200px; height: 900px; overflow: hidden;
    background: var(--page-bg);
  }
  .card {
    position: absolute; left: 110px; top: 170px;
    width: 980px; height: 560px;
    background: linear-gradient(180deg, var(--sky) 0%, var(--sky-deep) 100%);
    box-shadow: 0 18px 40px rgba(60, 40, 30, 0.25);
    overflow: hidden;
  }
  .card__band { position: absolute; inset: 0; }
  .medallion {
    position: absolute; left: 35px; top: 70px;
    width: 380px; height: 380px;
  }
  .medallion__art {
    position: absolute; left: 30px; top: 30px;
    width: 320px; height: 320px; border-radius: 50%;
    background: radial-gradient(circle at 50% 42%, var(--cupcake-pink) 0%, var(--cupcake-pink) 28%, var(--cupcake-cream) 62%, #ffffff 100%);
  }
  .details {
    position: absolute; left: 450px; top: 128px; width: 450px;
    text-align: center; color: var(--ink-pink);
  }
  .details__company {
    font-family: "Chewy", cursive; font-size: 42px; letter-spacing: 0.5px;
    line-height: 1;
  }
  .details__name {
    margin-top: 30px;
    font-family: "Chewy", cursive; font-size: 37px; line-height: 1;
  }
  .details__phone {
    margin-top: 26px;
    font-family: "Delius", sans-serif; font-size: 36px; letter-spacing: 2px; line-height: 1;
  }
  .details__acn {
    margin-top: 20px;
    font-family: "Delius", sans-serif; font-size: 36px; letter-spacing: 1px; line-height: 1;
  }
  .details__acn b { font-family: "Chewy", cursive; font-weight: 400; }
  .contact {
    position: absolute; bottom: 20px;
    font-family: "Delius", sans-serif; font-size: 27px; color: var(--ink-dark);
    letter-spacing: 0.5px;
  }
  .contact--web { left: 18px; }
  .contact--email { right: 18px; bottom: 48px; }
</style>
</head>
<body>
  <div class="card">
    <svg class="card__band" width="980" height="560" viewBox="0 0 980 560" aria-hidden="true">
      <rect x="0" y="105" width="980" height="300" fill="var(--band)"/>
      <rect x="0" y="125" width="980" height="260" fill="var(--band-light)" opacity="0.35"/>
      <rect x="0" y="92" width="980" height="16" fill="var(--lace)"/>
      <line x1="0" y1="100" x2="980" y2="100" stroke="var(--lace-white)" stroke-width="3" stroke-dasharray="3 5"/>
      <rect x="0" y="402" width="980" height="16" fill="var(--lace)"/>
      <line x1="0" y1="410" x2="980" y2="410" stroke="var(--lace-white)" stroke-width="3" stroke-dasharray="3 5"/>
    </svg>

    <div class="medallion">
      <svg width="380" height="380" viewBox="0 0 380 380" aria-hidden="true">
        <circle cx="190" cy="190" r="184" fill="var(--ring)"/>
        <circle cx="190" cy="190" r="172" fill="none" stroke="var(--lace-white)" stroke-width="4" stroke-dasharray="3 6"/>
        <circle cx="190" cy="190" r="164" fill="#ffffff"/>
      </svg>
      <div class="medallion__art" role="img" aria-label="Illustration of a pink frosted cupcake tied with a pink ribbon bow"></div>
    </div>

    <div class="details">
      <p class="details__company">Pindle's Bakery Pty Ltd</p>
      <p class="details__name">Maren Tulloch</p>
      <p class="details__phone">0412 506 218</p>
      <p class="details__acn"><b>ACN</b> 581 246 037</p>
    </div>

    <p class="contact contact--web">www.pindlesbakery.com.au</p>
    <p class="contact contact--email">maren@pindlesbakery.com.au</p>
  </div>
</body>
</html>
```